Hollow Meridian: Box for Fundlaunch Miniatures Game

We are a board game publisher based in México. Our most recent project is Hollow Meridian coming very soon to Fundlaunch.

About Hollow Meridian: which is an alternative XX century with cosmic horror and different events since 1918. The story takes place in 1984, Europe consumed by a fog which expands and corrupts/consumes everything. The world is divided in different superpowers now. Attached is a press kit with the general info of the setting. (HM - Press Kit English v2.pdf)
For more info, please visit https://www.pagebook.example/HollowMeridian/

About the design we need:
We need the front and back illustration for a 2-piece box with measures 30cm x 30cm x 10cm
For the visuals, we wish to have a minimalistic box that feels elegant. Instead of having a colorful action shot displayed in the cover.

The box should include the Game logo (Hollow Meridian (Logo v2).png)

And the texture must display a dark swamp-like landscape with a lot of fog, mist (the miasma that consumed Europe; reference image). Dark silhouettes are visible in the fog; maybe plants, deteriorated European buildings or monsters (from the ones in the file Monsters.zip) IMPORTANT: The viewer should feel inside of the forest and the miasma, so he is not able to see the sky or the top of the trees. The monsters are near, far, to the sides, everywhere. Silhouettes can have different transparency levels to display this.

Include a lot of the fog! (Miasma)

The overall feel should be Mysterious, Horror, Macabre and Epic.
The predominant color for the box should be dark. Maybe black.

Attached is a file with references of minimalistic boxes we like, textures and examples for the illustrations of the game (References for box.jpg)

The bottom part should also include a similar illustration but not the same. (Display different silhouettes, etc). Please provide some frames with placeholder texts for the product description, images or similar.

For the sides, we are open to see suggestions, whether you decide it to be an extent of the cover illustration; fade to black or another color; or make its own illustration with the same texture.

After this stage, we desire to keep working with designers for other things we need. The layout designer will place all the information in the back of the box (Barcode, blurb, specs, company, etc)

This box is for a skirmish game with miniatures and people who enjoy stories, role playing games, and miniatures wargaming. We expect to launch the Fundlaunch on July 17th.

IF POSSIBLE, please show progress as a mock-up of the 3D box.

Don't hesitate to reach out if you have questions.

Target Market(s)

Board gamers. Geek. Adults between 25 and 35.
People who enjoy from the Vorbex universe or fantasy/sci fi movies or tv shows.

Industry/Entity Type

Entertainment

Font styles to use
Serif
Other font styles liked:
• Horror Mystery or epic feel

Colors
333333
6b449b
0355a3
000000
00a990

Requirements
Must have
• Horror/Mystery/Epic feel. The viewers must feel that inside of the box, they will find all three of these.
• The fog and miasma in the texture.
Nice to have
• An elegant choice of the silhouettes, preferably in different poses than the files provided but still recognisable when the viewer sees the content and the silhouettes. Even new monstrous silohuettes are welcome and we might consider creating content for it.
• Maybe the color palette or style of the reference file.

```html
<!DOCTYPE html>
<html lang="en">
<head>
<meta charset="utf-8">
<title>Hollow Meridian – Box Back</title>
<link rel="stylesheet" href="https://fonts.googleapis.com/css2?family=EB+Garamond:wght@400;600&family=Uncial+Antiqua&display=swap">
<style>
  :root {
    --stage: #e4e4e4;
    --ink-black: #050607;
    --fog-grey: #8e949a;
    --fog-violet: #6b449b;
    --fog-green: #4d7a55;
    --panel-black: #060707;
    --frame-silver: #a9acaa;
    --frame-dark: #4a4d4c;
    --heading-green: #6fb152;
    --body-text: #d8d8d4;
    --slot-grey: #4a5053;
  }
  html, body {
    margin: 0;
    width: 1200px;
    height: 1200px;
    overflow: hidden;
    background: var(--stage);
  }
  .box-back {
    position: absolute;
    left: 40px;
    top: 40px;
    width: 1120px;
    height: 1120px;
    overflow: hidden;
    background: var(--ink-black);
    font-family: "EB Garamond", Georgia, serif;
  }
  .miasma-scene {
    position: absolute;
    inset: 0;
    background:
      radial-gradient(ellipse 40% 26% at 38% 20%, rgba(90,140,95,.7), transparent 70%),
      radial-gradient(ellipse 38% 24% at 70% 12%, rgba(120,110,175,.6), transparent 70%),
      radial-gradient(ellipse 30% 18% at 18% 8%, rgba(60,95,70,.6), transparent 70%),
      radial-gradient(ellipse 20% 28% at 33% 52%, rgba(100,62,55,.6), transparent 70%),
      radial-gradient(ellipse 60% 14% at 28% 70%, rgba(150,155,160,.45), transparent 70%),
      radial-gradient(ellipse 45% 10% at 80% 80%, rgba(150,155,160,.35), transparent 70%),
      radial-gradient(ellipse 35% 12% at 10% 60%, rgba(120,125,130,.35), transparent 70%),
      linear-gradient(180deg, #1c2422 0%, #181c1f 45%, #0b0d0e 75%, #050607 100%);
  }
  .fog-layer {
    position: absolute;
    inset: 0;
    width: 100%;
    height: 100%;
    mix-blend-mode: screen;
    opacity: .55;
  }
  .story-panel {
    position: absolute;
    left: 54%;
    top: 15%;
    width: 38%;
    box-sizing: border-box;
    background: var(--panel-black);
    border: 6px double var(--frame-silver);
    outline: 3px solid var(--frame-dark);
    padding: 78px 30px 30px;
    text-align: center;
    color: var(--body-text);
  }
  .game-title {
    position: absolute;
    left: 50%;
    top: -36px;
    transform: translateX(-50%);
    width: 240px;
    padding: 10px 0;
    background: var(--frame-dark);
    border: 2px solid var(--frame-silver);
    color: var(--body-text);
    font-size: 30px;
    line-height: 1.05;
  }
  .section-heading {
    margin: 0 0 18px;
    font-family: "Uncial Antiqua", serif;
    font-weight: 400;
    color: var(--heading-green);
    font-size: 20px;
  }
  .story-panel p {
    margin: 0 0 26px;
    font-size: 17px;
    line-height: 1.55;
  }
  .story-panel p:last-child { margin-bottom: 0; }
  .feature-block {
    position: absolute;
    left: 5%;
    top: 73%;
    width: 90%;
    color: var(--body-text);
  }
  .feature-block .section-heading { margin-bottom: 10px; }
  .feature-block p {
    margin: 0;
    font-size: 18px;
    line-height: 1.4;
  }
  .image-slots {
    position: absolute;
    left: 5%;
    right: 5%;
    top: 85%;
    height: 11.5%;
    display: flex;
    gap: 2.4%;
  }
  .image-slot {
    flex: 1;
    background: var(--slot-grey);
  }
</style>
</head>
<body>
  <main class="box-back">
    <div class="miasma-scene" role="img" aria-label="Dark fog-filled forest with bare trees and an antlered, tentacled monster stag in the mist">
      <svg class="fog-layer" viewBox="0 0 1120 1120" preserveAspectRatio="none" aria-hidden="true">
        <defs>
          <filter id="mist" x="0" y="0" width="100%" height="100%">
            <feTurbulence type="fractalNoise" baseFrequency="0.004 0.009" numOctaves="4" seed="7"/>
            <feColorMatrix values="0 0 0 0 0.62  0 0 0 0 0.64  0 0 0 0 0.68  0 0 0 1.6 -0.75"/>
          </filter>
          <linearGradient id="mist-fade" x1="0" y1="0" x2="0" y2="1">
            <stop offset="0" stop-color="#fff" stop-opacity=".6"/>
            <stop offset=".7" stop-color="#fff" stop-opacity="1"/>
            <stop offset="1" stop-color="#fff" stop-opacity=".3"/>
          </linearGradient>
          <mask id="mist-mask"><rect width="1120" height="1120" fill="url(#mist-fade)"/></mask>
        </defs>
        <rect width="1120" height="1120" filter="url(#mist)" mask="url(#mist-mask)"/>
      </svg>
    </div>

    <section class="story-panel">
      <div class="game-title">Hollow<br>Meridian</div>
      <h2 class="section-heading">Into the Lost Continent</h2>
      <p>Lorem ipsum dolor sit amet, consectetur adipiscing elit, sed do eiusmod tempor incididunt ut labore et dolore magna aliqua. Ut enim ad minim veniam, quis nostrud exercitation ullamco laboris nisi ut aliquip ex ea commodo consequat. Duis aute irure dolor in reprehenderit in voluptate velit esse cillum dolore eu fugiat nulla pariatur. Excepteur sint occaecat cupidatat non proident, sunt in culpa qui officia deserunt mollit anim id est laborum.</p>
      <p>Lorem ipsum dolor sit amet, consectetur adipiscing elit, sed do eiusmod tempor incididunt ut labore et dolore magna aliqua. Ut enim ad minim veniam, quis nostrud exercitation ullamco laboris nisi ut aliquip ex ea commodo consequat. Duis aute irure dolor in reprehenderit in voluptate velit esse cillum dolore eu fugiat nulla pariatur.</p>
    </section>

    <section class="feature-block">
      <h2 class="section-heading">Into the Lost Continent</h2>
      <p>Lorem ipsum dolor sit amet, consectetur adipiscing elit, sed do eiusmod tempor incididunt ut labore et dolore magna aliqua. Ut enim ad minim veniam, quis nostrud exercitation ullamco laboris nisi ut aliquip ex ea commodo consequat. Duis aute irure dolor in reprehenderit in voluptate velit esse cillum dolore eu fugiat nulla pariatur. Excepteur sint occaecat cupidatat non proident.</p>
    </section>

    <div class="image-slots">
      <div class="image-slot"></div>
      <div class="image-slot"></div>
      <div class="image-slot"></div>
      <div class="image-slot"></div>
      <div class="image-slot"></div>
    </div>
  </main>
</body>
</html>
```